New Creative Busines Card

Hi Lead Designer,

How are you going?

I was hoping you can help me design the perfect business card for my new business. I have listed below some background information about the business and the concept to help with your design. I'm open to any form of creative ideas, but would like to have two types of colour schemes one dark color and one light.

I would like to have a dark set of design and a light (One design with one in black or dark background and one with light background to compare the contrast since the business card will be double sided one) I imagine this will be pretty easy to change the background of the design. Would prefer one side to have all the details and the other will just have a amazing logo (K7) to give it the finishing touch.

Feel free to email me if you have any questions.

Business Structure and design concepts:

Name of the business: K7 Advisory
Business: Dating agency and event management (Date night etc)
Concept: The main focus will be the K7 ( As some sort of a heart shape like logo) be creative
Details to include in the card will be general details like Name, Title: , Email, mobile, website (Contact details will be given later).

The rest of the idea is up to you, feel free to go crazy with your creative ideas.

Thank you for your help in advance, may the best candidate win~!

Target Market(s)

Target market will be Professional, Elegant, young and ambitious people.

Industry/Entity Type

Business

Requirements
Must have
• Focus on the K7 (as some sort of a heart shape logo). Since this is a double sides design would prefer on one side to focus on the just the K7 logo and the other side with a smaller version of the logo (with it or without) and all the details such as Name, Title, Mobile, Email, Website. Please have the design in landscape format.Not fuss with the Font as long as it is easy to read.
Nice to have
• Different Contrast in colours (keep it simple) one side dark colour scheme and one side light. Prefer to have 3-4 colours (not overwhelm with too many colours) to keep it simple and elegant.
Should not have
• Too colours, main focus is should be the K7 logo not the colours

```html
<!DOCTYPE html>
<html lang="en">
<head>
<meta charset="utf-8">
<title>K7 Advisory — Business Card</title>
<link rel="stylesheet" href="https://fonts.googleapis.com/css2?family=Great+Vibes&family=Open+Sans:wght@300;400;600&display=swap">
<style>
  :root {
    --red: #e0242b;
    --red-deep: #b5161c;
    --red-soft: #ef4a4f;
    --paper: #f7f7f5;
    --ink: #555555;
    --stage: #e6e6e6;
  }
  * { box-sizing: border-box; margin: 0; padding: 0; }
  html, body { width: 1169px; height: 1200px; overflow: hidden; }
  body {
    background: var(--stage);
    font-family: "Open Sans", Arial, sans-serif;
    position: relative;
  }
  .card {
    position: absolute;
    left: 134px;
    width: 900px;
    height: 515px;
    border-radius: 34px;
    overflow: hidden;
    box-shadow: 0 6px 18px rgba(0,0,0,0.18);
  }
  .card--front { top: 50px; }
  .card--back { top: 630px; background: var(--paper); }

  .front-pattern {
    position: absolute; inset: 0;
    background: radial-gradient(circle at 30% 25%, var(--red-soft) 0%, var(--red) 45%, var(--red-deep) 100%);
  }
  .brand-badge {
    position: absolute;
    left: 300px; top: 70px;
    width: 300px; height: 300px;
    border-radius: 50%;
    background: var(--paper);
    box-shadow: inset 0 4px 10px rgba(0,0,0,0.25);
    display: flex; align-items: center; justify-content: center;
  }
  .brand-name {
    font-family: "Open Sans", Arial, sans-serif;
    font-weight: 600;
    font-size: 40px;
    color: var(--red);
  }
  .front-tagline {
    position: absolute;
    left: 0; right: 0; bottom: 58px;
    text-align: center;
    color: #ffffff;
    font-size: 36px;
    font-weight: 400;
    letter-spacing: 1px;
  }

  .back-wave { position: absolute; inset: 0; }
  .holder {
    position: absolute; left: 250px; top: 90px;
  }
  .holder-name {
    font-family: "Great Vibes", cursive;
    font-size: 56px;
    color: var(--red);
    line-height: 1;
  }
  .holder-title {
    font-size: 26px; font-weight: 300;
    color: var(--red);
    margin-left: 40px;
  }
  .contact-list {
    position: absolute; left: 56px; top: 250px;
    list-style: none;
  }
  .contact-list li {
    display: flex; align-items: center; gap: 16px;
    font-size: 20px; color: var(--ink);
    margin-bottom: 14px;
  }
  .icon-dot {
    width: 30px; height: 30px; border-radius: 50%;
    background: var(--red);
    display: flex; align-items: center; justify-content: center;
    flex: none;
  }
  .brand-badge--small {
    left: 600px; top: 170px;
    width: 200px; height: 200px;
  }
  .brand-badge--small .brand-name { font-size: 28px; }
  .web-list {
    position: absolute; right: 56px; bottom: 42px;
    list-style: none; text-align: right;
  }
  .web-list li {
    display: flex; align-items: center; justify-content: flex-end; gap: 14px;
    font-size: 20px; color: var(--ink);
    margin-top: 10px;
  }
  .plain-dot {
    width: 22px; height: 22px; border-radius: 50%;
    background: var(--red); flex: none;
  }
</style>
</head>
<body>
  <section class="card card--front">
    <div class="front-pattern" role="img" aria-label="Soft scattered heart pattern in red tones"></div>
    <div class="brand-badge"><span class="brand-name">K7 Advisory</span></div>
    <p class="front-tagline">Dating agency and event management</p>
  </section>

  <section class="card card--back">
    <svg class="back-wave" width="900" height="515" viewBox="0 0 900 515" aria-hidden="true">
      <path d="M0 0 H900 V330 C820 330 720 250 640 170 C560 90 360 40 0 110 Z" fill="var(--red)"/>
    </svg>
    <div class="holder">
      <p class="holder-name">Marlen Vance</p>
      <p class="holder-title">owner/creator</p>
    </div>
    <ul class="contact-list">
      <li>
        <span class="icon-dot">
          <svg width="16" height="16" viewBox="0 0 16 16"><path d="M4 1 L6.5 4 L5 6 C6 8.5 7.5 10 10 11 L12 9.5 L15 12 L13 15 C7 15 1 9 1 3 Z" fill="#fff"/></svg>
        </span>
        555.310.4826
      </li>
      <li>
        <span class="icon-dot">
          <svg width="16" height="12" viewBox="0 0 16 12"><rect x="1" y="1" width="14" height="10" fill="none" stroke="#fff" stroke-width="1.6"/><path d="M1 1 L8 7 L15 1" fill="none" stroke="#fff" stroke-width="1.6"/></svg>
        </span>
        hello@k7advisory.com
      </li>
    </ul>
    <div class="brand-badge brand-badge--small"><span class="brand-name">K7 Advisory</span></div>
    <ul class="web-list">
      <li>social.com / k7advisory <span class="plain-dot"></span></li>
      <li>48 Larkspur Ave Milton, Ont L9T 2K4
        <svg width="22" height="28" viewBox="0 0 22 28"><path d="M11 1 C5 1 1 5.5 1 11 C1 18 11 27 11 27 C11 27 21 18 21 11 C21 5.5 17 1 11 1 Z" fill="var(--red)"/><circle cx="11" cy="11" r="4" fill="#fff"/></svg>
      </li>
    </ul>
  </section>
</body>
</html>
```